Business Cards Needed For Veterinary Business

Looking for a business card design for a veterinary blood bank. We would like it to be clean and professional on appearance but still warm and inviting. We would like to utilize our logo and similar coloring. We will use our phone number, email, website, employee name, employee title.

We do not want a bunch of animated animal photos but do not need the style to be as clinical as a laboratory or human medical procedure office.

We are looking for some creative ideas to choose from so that we can generate a standout professional business card for our management team to utilize.

Target Market(s)

professionals

Industry/Entity Type

veterinary

Contact Information for Business Card

employee name, employee title, phone number, website URL, email

Font styles to use
Sans Serif

Colors
0054AA
0677BA
7BADD7
CADEEF
E8F1F8
EB3D1F
EC4F4E
F09395
F8D3D4
FCEDEE

Requirements
Nice to have
• creative design
Should not have
• animated photos

```html
<!DOCTYPE html>
<html lang="en">
<head>
<meta charset="utf-8">
<title>Pinecrest Animal Blood Bank – Business Cards</title>
<link rel="stylesheet" href="https://fonts.googleapis.com/css2?family=Montserrat:wght@400;500;700;800&display=swap">
<style>
  :root {
    --backdrop: #3b3c3f;
    --card-white: #ffffff;
    --navy-deep: #001a33;
    --navy-mid: #022a4d;
    --brand-red: #eb3d1f;
    --alert-red: #ec2f3a;
    --ink-grey: #3a3a3a;
    --text-dark: #222222;
  }
  * { box-sizing: border-box; margin: 0; padding: 0; }
  html, body {
    width: 1200px; height: 1200px; overflow: hidden;
    background: var(--backdrop);
    font-family: "Montserrat", sans-serif;
  }
  .canvas {
    width: 1200px; height: 1200px;
    display: flex; flex-direction: column; align-items: center; justify-content: center;
    gap: 40px;
  }
  .card {
    width: 900px; height: 514px;
    border-radius: 38px;
    position: relative;
    overflow: hidden;
    box-shadow: 0 14px 30px rgba(0,0,0,.35);
  }
  .card--front { background: var(--card-white); }
  .card--back {
    background: radial-gradient(ellipse at 50% 45%, var(--navy-mid) 0%, var(--navy-deep) 70%);
    display: flex; align-items: center; justify-content: center;
  }

  .brand {
    display: flex; align-items: center; gap: 16px;
    color: var(--alert-red);
    font-weight: 800;
    letter-spacing: .5px;
  }
  .brand__dot {
    border-radius: 50%;
    background: var(--alert-red);
    flex: none;
  }
  .card--front .brand {
    position: absolute; right: 70px; top: 120px;
    font-size: 30px; line-height: 1.1; max-width: 380px;
  }
  .card--front .brand__dot { width: 46px; height: 46px; }
  .card--back .brand { font-size: 52px; line-height: 1.1; max-width: 640px; }
  .card--back .brand__dot { width: 80px; height: 80px; }

  .person {
    position: absolute; left: 70px; bottom: 70px;
  }
  .person__name {
    color: var(--alert-red);
    font-weight: 700;
    font-size: 56px;
    line-height: 1;
    letter-spacing: -1px;
  }
  .person__title {
    color: var(--ink-grey);
    font-weight: 400;
    font-size: 34px;
    margin-top: 6px;
    margin-bottom: 18px;
  }
  .contact { list-style: none; }
  .contact__item {
    display: flex; align-items: center; gap: 16px;
    font-size: 30px; color: var(--text-dark);
    font-weight: 500;
    line-height: 1.35;
  }
  .contact__icon { width: 30px; height: 30px; flex: none; fill: var(--alert-red); }
  .contact__icon--line { fill: none; stroke: var(--alert-red); stroke-width: 2.2; }
</style>
</head>
<body>
<main class="canvas">

  <section class="card card--front" aria-label="Business card front">
    <div class="brand">
      <span class="brand__dot"></span>
      <span class="brand__name">Pinecrest Animal Blood Bank</span>
    </div>

    <div class="person">
      <h1 class="person__name">FULL NAME</h1>
      <p class="person__title">TITLE</p>
      <ul class="contact">
        <li class="contact__item">
          <svg class="contact__icon" viewBox="0 0 24 24" aria-hidden="true">
            <path d="M6.6 10.8c1.4 2.8 3.8 5.1 6.6 6.6l2.2-2.2c.3-.3.7-.4 1-.2 1.1.4 2.3.6 3.6.6.6 0 1 .4 1 1V20c0 .6-.4 1-1 1C10.6 21 3 13.4 3 4c0-.6.4-1 1-1h3.5c.6 0 1 .4 1 1 0 1.3.2 2.5.6 3.6.1.3 0 .7-.2 1z"/>
          </svg>
          <span>(000) 000 0000</span>
        </li>
        <li class="contact__item">
          <svg class="contact__icon" viewBox="0 0 24 24" aria-hidden="true">
            <path d="M2 5h20v14H2z M3.5 6.5 12 13l8.5-6.5" fill="var(--alert-red)"/>
            <path d="M3 6l9 7 9-7" fill="none" stroke="#fff" stroke-width="1.6"/>
          </svg>
          <span>email@company.com</span>
        </li>
        <li class="contact__item">
          <svg class="contact__icon contact__icon--line" viewBox="0 0 24 24" aria-hidden="true">
            <circle cx="12" cy="12" r="9.5"/>
            <ellipse cx="12" cy="12" rx="4.2" ry="9.5"/>
            <path d="M2.5 12h19M4 7h16M4 17h16"/>
          </svg>
          <span>www.company.com</span>
        </li>
      </ul>
    </div>
  </section>

  <section class="card card--back" aria-label="Business card back">
    <div class="brand">
      <span class="brand__dot"></span>
      <span class="brand__name">Pinecrest Animal Blood Bank</span>
    </div>
  </section>

</main>
</body>
</html>
```